Criação de Papelaria Profissional para Contabilidade & Finanças
" ESTOU INICANDO AGORA O ESCRITORIO DE CONTABILIDADE, QUERO ATUAR NO RAMO DE TREINAMENTO ATRAVÉS DO COACHING , FAZER CONSULTORIAS NA AREA CONTABIL, SERVIÇOS CONTABEIS EM GERAL, DESDE O MICROEMPREENDEDOR ATÉ O A EMPRESA DE GRANDE PORTE LUCRO REAL "

```html
<!DOCTYPE html>
<html lang="pt-BR">
<head>
<meta charset="utf-8">
<title>NVC Consultoria Contábil &amp; Fiscal — Papelaria</title>
<link rel="stylesheet" href="https://fonts.googleapis.com/css2?family=Montserrat:wght@500;600;700;800&display=swap">
<style>
  :root{
    --bg:#ffffff;
    --paper:#f7f7f8;
    --paper-shade:#e4e5e8;
    --navy:#0d1530;
    --navy-deep:#070c1e;
    --navy-light:#1b2a55;
    --gold:#d3a73a;
    --gold-soft:#b08a34;
    --ink:#4a4d57;
  }
  *{box-sizing:border-box;margin:0;padding:0}
  html,body{width:1200px;height:1200px;overflow:hidden;background:var(--bg)}
  body{position:relative;font-family:"Montserrat",sans-serif}

  .sheet{position:absolute;top:180px;width:552px;height:876px;overflow:hidden;
    box-shadow:0 6px 18px rgba(0,0,0,.18)}
  .letterhead{left:34px;background:linear-gradient(180deg,#ffffff 0%,var(--paper) 60%,#efeff1 100%)}
  .folder{left:614px;background:radial-gradient(ellipse at 60% 40%,var(--navy-light) 0%,var(--navy) 45%,var(--navy-deep) 100%)}

  .pattern{position:absolute;left:0;top:0;height:700px}
  .letterhead .pattern{width:280px;background:linear-gradient(100deg,var(--paper-shade) 0%,rgba(228,229,232,.35) 60%,rgba(255,255,255,0) 100%)}
  .folder .pattern{left:14px;top:70px;width:170px;height:640px;background:linear-gradient(100deg,rgba(40,58,110,.55) 0%,rgba(30,45,90,.2) 70%,rgba(13,21,48,0) 100%)}

  .brand{position:absolute;display:flex;align-items:center;gap:8px}
  .brand-mark{background:var(--gold)}
  .brand-name{color:var(--gold);font-weight:800;letter-spacing:.02em;line-height:1}
  .brand-tag{color:var(--gold);font-weight:600;letter-spacing:.06em;text-transform:uppercase}

  .letterhead .brand{left:174px;top:710px}
  .letterhead .brand-mark{width:18px;height:18px}
  .letterhead .brand-name{font-size:34px;color:var(--navy)}
  .letterhead .brand-tag{position:absolute;left:200px;top:752px;font-size:6.5px;color:var(--ink)}

  .contacts{position:absolute;left:92px;right:40px;top:800px;display:flex;justify-content:space-between;
    font-size:7.5px;color:var(--ink);line-height:1.5}
  .contact{display:flex;gap:5px;align-items:flex-start}
  .contact-dot{width:10px;height:10px;border-radius:50%;background:var(--navy);flex:none;margin-top:2px}

  .rule{position:absolute;left:0;right:0;height:3px;background:linear-gradient(90deg,var(--gold-soft),var(--gold),var(--gold-soft))}
  .band{position:absolute;left:0;right:0;bottom:0;height:24px;background:var(--navy)}
  .letterhead .rule{top:828px}
  .folder .rule{top:536px;opacity:.7}
  .folder .band{background:var(--navy-deep);height:30px;border-top:2px solid var(--gold-soft)}

  .folder .brand{left:205px;top:440px}
  .folder .brand-mark{width:30px;height:30px}
  .folder .brand-name{font-size:80px}
  .folder .brand-tag{position:absolute;left:245px;top:524px;font-size:10.5px}

  .product{position:absolute;left:334px;top:696px;width:190px;height:132px;border-radius:10px;
    background:linear-gradient(90deg,#05091a 0%,#1c2850 45%,#0a1128 100%);display:flex;align-items:center;justify-content:center}
  .product .brand{position:static}
  .product .brand-mark{width:10px;height:10px}
  .product .brand-name{font-size:26px}
</style>
</head>
<body>

<section class="sheet letterhead" aria-label="Papel timbrado">
  <div class="pattern" role="img" aria-label="Padrão decorativo de setas em tons de cinza claro"></div>
  <div class="brand"><span class="brand-mark"></span><span class="brand-name">NVC</span></div>
  <span class="brand-tag">Consultoria Contábil &amp; Fiscal</span>
  <div class="contacts">
    <div class="contact"><span class="contact-dot"></span><span>(41) 3000-0000<br>(41) 99000-0000</span></div>
    <div class="contact"><span class="contact-dot"></span><span>Rua das Acácias, 120 · Centro<br>Curitiba PR · CEP 80000-000</span></div>
    <div class="contact"><span class="contact-dot"></span><span>www.nvccontabil.com.br<br>contato@nvccontabil.com.br</span></div>
  </div>
  <div class="rule"></div>
  <div class="band"></div>
</section>

<section class="sheet folder" aria-label="Pasta">
  <div class="pattern" role="img" aria-label="Padrão decorativo de setas em azul escuro"></div>
  <div class="brand"><span class="brand-mark"></span><span class="brand-name">NVC</span></div>
  <span class="brand-tag">Consultoria Contábil &amp; Fiscal</span>
  <div class="product" role="img" aria-label="Embalagem escura com a marca">
    <div class="brand"><span class="brand-mark"></span><span class="brand-name">NVC</span></div>
  </div>
  <div class="band"></div>
</section>

</body>
</html>
```